Chemical Distribution Company Needs a Website

We need a website designed for an existing company based in Michigan. We have grown substantially since inception and we need our website to reflect this growth. It currently has a very mom and pop feel to it. What we do is ship chemicals in Drums, Totes, Bags, Bulk Tank Trucks, and rail from our warehouses in Toledo Oh, and Chicago il. This will be a site that strictly shows what we do and will not be E-commerced based. The final design should communicate a large business with NorthAmerican reach and worldwide sourcing capabilities.

Target Market(s)

What we sell are chemicals such as acids, solvents, oils, and salts all of which are used in the manufacturing process of various products from steel to car parts to paint to car wash soaps to food. We are trying to look like a large company that has stability and track record to go after all types of industries and manufacturers

Industry/Entity Type

It Company

Number of Pages Required

5+ page

Font styles to use
Serif
Sans Serif

Requirements
Must have
• Be Formatted for WIX as that is what we use to Host and Build. Unless you have a better idea. I would also like it to be viewed on a mobile platform which it is not now.
• Tabs for:
• Home Page (similar to "www.pellwinstock.com")
• Who we are- with subtabs for (Overview, Leadership, and Capabilities)
• Chemicals- (subtabs for (overview, Chemicals A-Z) Look at Pellwinstock.com
• Metal Working Lubricants (with a drop down identical to the products tab at "www.ravenforgeoil.com"
• Contact- Very similar to www.tarvikmenta.com/contact/
• Need to have professional photos of Chemical Facilities, Bulk Tanks Trucks, Chemical Railcars, Storage Facilities filled with Drums and Totes, a Tank Farm.
Nice to have
• Want to have our site look like a combination of tarvikmenta.com, pellwinstock.com, and brolandquintec.com

```html
<!DOCTYPE html>
<html lang="en">
<head>
<meta charset="utf-8">
<title>Marlow Chemicals</title>
<link href="https://fonts.googleapis.com/css2?family=Lato:wght@400;700&family=Raleway:wght@500;700&display=swap" rel="stylesheet">
<style>
:root{
  --sky:#23a8f2;
  --navy:#043e5f;
  --deep:#0c3550;
  --header:#e6ebee;
  --ink:#2a4a60;
  --white:#ffffff;
  --muted:#c5d6e2;
}
*{margin:0;padding:0;box-sizing:border-box}
html,body{width:1200px;height:1049px;overflow:hidden}
body{position:relative;font-family:'Lato',sans-serif;background:var(--navy);color:var(--white)}
.site-header{position:absolute;top:0;left:0;width:1200px;height:104px;background:var(--header);}
.brand{position:absolute;left:49px;top:30px;display:flex;align-items:center;gap:12px}
.brand-mark{width:40px;height:40px;border-radius:50%;background:var(--sky)}
.brand-text{display:flex;flex-direction:column}
.brand-name{font-family:'Raleway',sans-serif;font-weight:700;font-size:27px;color:var(--navy);letter-spacing:.5px;line-height:1}
.brand-tag{font-size:7px;color:var(--sky);letter-spacing:1px;text-transform:uppercase;margin-top:3px}
.nav-home{position:absolute;left:420px;top:0;width:70px;height:104px;background:var(--sky);color:var(--white);font-size:14px;display:flex;align-items:center;justify-content:center}
.main-nav{position:absolute;left:526px;top:41px;display:flex;font-size:14px;color:var(--ink)}
.main-nav span{white-space:nowrap}
.main-nav .sep{margin:0 24px}
.nav-tools{position:absolute;left:1065px;top:43px;display:flex;gap:18px}
.hero{position:absolute;top:104px;left:0;width:1200px;height:574px;background:linear-gradient(120deg,#3a6d8f 0%,#2b5d80 40%,#3f6f8c 70%,#2e5a78 100%)}
.hero-copy{position:absolute;top:160px;left:0;width:1200px;text-align:center}
.hero-title{font-family:'Raleway',sans-serif;font-weight:700;font-size:43px;letter-spacing:.5px}
.hero-text{width:700px;margin:12px auto 0;font-size:15px;line-height:22.7px}
.btn{display:inline-block;margin-top:40px;width:133px;height:41px;line-height:41px;background:var(--sky);font-size:14px;text-transform:uppercase}
.band-line{position:absolute;top:677px;left:0;width:1200px;height:3px;background:var(--white)}
.feature{position:absolute;top:612px;width:300px;text-align:center}
.feature-badge{width:142px;height:142px;margin:0 auto;border-radius:50%;background:var(--sky);border:3px solid var(--white);display:flex;align-items:center;justify-content:center}
.feature-title{margin-top:40px;font-family:'Raleway',sans-serif;font-weight:500;font-size:20px;text-transform:uppercase}
.feature-text{margin:12px auto 0;width:270px;font-size:12.5px;line-height:17px;color:var(--muted)}
.feature-more{margin-top:14px;font-size:12.5px;font-weight:700;text-transform:uppercase}
.site-footer{position:absolute;top:970px;left:0;width:1200px;height:79px;background:var(--sky)}
.copyright{position:absolute;left:50px;top:30px;font-size:13px}
.social{position:absolute;right:50px;top:31px;display:flex;gap:24px;align-items:center}
.social i{display:block;width:14px;height:14px;border-radius:50%;background:#b8e2fa}
</style>
</head>
<body>
<header class="site-header">
  <div class="brand"><span class="brand-mark"></span><div class="brand-text"><span class="brand-name">MARLOW CHEMICALS</span><span class="brand-tag">Setting the industry standard for customer service</span></div></div>
  <div class="nav-home">Home</div>
  <nav class="main-nav"><span>Who we are</span><span class="sep">|</span><span>Chemicals</span><span class="sep">|</span><span>Metal Working Lubricants</span><span class="sep">|</span><span>Contact</span><span class="sep">|</span></nav>
  <div class="nav-tools">
    <svg width="15" height="14" viewBox="0 0 15 14"><rect x="1" y="2" width="13" height="10" fill="#0b2233"/><path d="M1 2l6.5 5L14 2" stroke="#e6ebee" stroke-width="1.4" fill="none"/></svg>
    <svg width="15" height="14" viewBox="0 0 15 14"><circle cx="6" cy="6" r="4" stroke="#0b2233" stroke-width="2" fill="none"/><path d="M9 9l4 4" stroke="#0b2233" stroke-width="2.2"/></svg>
    <svg width="13" height="14" viewBox="0 0 13 14"><circle cx="6.5" cy="4" r="3" fill="#0b2233"/><path d="M1 13c0-4 2-6 5.5-6S12 9 12 13z" fill="#0b2233"/></svg>
  </div>
</header>

<section class="hero" role="img" aria-label="Photo of a chemical processing plant with a worker beside steel tanks">
  <div class="hero-copy">
    <h1 class="hero-title">Consectetur Adipiscing Elit</h1>
    <p class="hero-text">Lorem ipsum dolor sit amet, consectetur adipiscing elit, sed do eiusmod tempor incididunt ut labore et dolore magna aliqua. Ut enim ad minim veniam, quis nostrud exercitation ullamco laboris nisi ut aliquip ex ea commodo consequat</p>
    <a class="btn">Read More</a>
  </div>
</section>
<div class="band-line"></div>

<div class="feature" style="left:96px">
  <div class="feature-badge"><svg width="90" height="80" viewBox="0 0 90 80" fill="none" stroke="#fff" stroke-width="4"><circle cx="32" cy="48" r="26"/><ellipse cx="32" cy="48" rx="12" ry="26"/><path d="M6 48h52M10 36h44M10 60h44"/><circle cx="60" cy="24" r="16" fill="#23a8f2" stroke-width="6"/><path d="M72 36l12 12" stroke-width="8"/></svg></div>
  <h2 class="feature-title">Overview</h2>
  <p class="feature-text">Lorem ipsum dolor sit amet, consectetur adipiscing elit, sed do eiusmod tempor incidi-dunt ut labore et dolore magna aliqua.</p>
  <p class="feature-more">More &#9656;</p>
</div>
<div class="feature" style="left:456px">
  <div class="feature-badge"><svg width="84" height="64" viewBox="0 0 84 64" fill="#fff"><circle cx="20" cy="14" r="8"/><circle cx="64" cy="14" r="8"/><path d="M4 56c0-18 6-26 16-26s16 8 16 26zM48 56c0-18 6-26 16-26s16 8 16 26z"/><circle cx="42" cy="12" r="10"/><path d="M24 62c0-22 8-32 18-32s18 10 18 32z" stroke="#23a8f2" stroke-width="2"/></svg></div>
  <h2 class="feature-title">Leadership</h2>
  <p class="feature-text">Lorem ipsum dolor sit amet, consectetur adipiscing elit, sed do eiusmod tempor incidi-dunt ut labore et dolore magna aliqua. Ut</p>
  <p class="feature-more">More &#9656;</p>
</div>
<div class="feature" style="left:810px">
  <div class="feature-badge"><svg width="74" height="80" viewBox="0 0 74 80" fill="#fff"><path d="M36 4C16 4 6 18 6 34c0 10 5 16 9 22v20h32V66h10c4 0 6-3 6-7V50l6-3-6-12C63 16 53 4 36 4z"/><circle cx="28" cy="34" r="9" fill="#23a8f2"/><circle cx="28" cy="34" r="4" fill="#fff"/><circle cx="46" cy="22" r="7" fill="#23a8f2"/><circle cx="46" cy="22" r="3" fill="#fff"/></svg></div>
  <h2 class="feature-title">Capabilities</h2>
  <p class="feature-text">Lorem ipsum dolor sit amet, consectetur adipiscing elit, sed do eiusmod tempor incidi-dunt ut labore et dolore magna aliqua.</p>
  <p class="feature-more">More &#9656;</p>
</div>

<footer class="site-footer">
  <p class="copyright">All Rights Reserved. Copyrights @ company Name. 2016</p>
  <div class="social">
    <svg width="14" height="14" viewBox="0 0 14 14" fill="none" stroke="#fff" stroke-width="2"><circle cx="2.5" cy="11.5" r="1.5" fill="#fff" stroke="none"/><path d="M1 6a7 7 0 0 1 7 7M1 1a12 12 0 0 1 12 12"/></svg>
    <i></i><i></i><i></i><i></i>
  </div>
</footer>
</body>
</html>
```